Design a Professional Business Card for Velmora Arcs

Design a business card for Velmora Arcs, we are a National Sport Court Company.

West Region Address: 4175 Quill Harbor Ln, Suite #215 Englewood, Colorado 80467
East Region Address: 3817 Tamsin Rd E, Bradenton, Florida 34583

Target Market(s)

High End Residential & Institutional Clients

Industry/Entity Type

Design & Construction

Contact Information for Business Card

Logo/Brand/Colors/ name, number (provided in comments)

Requirements
Must have
• Colors only provided in logo
Should not have
• Any other colors not in existing logo (attached)

```html
<!DOCTYPE html>
<html lang="en">
<head>
<meta charset="utf-8">
<title>Velmora Arcs — Business Card</title>
<link href="https://fonts.googleapis.com/css2?family=Montserrat:wght@400;600;700&display=swap" rel="stylesheet">
<style>
  :root {
    --navy: #163563;
    --green: #036b37;
    --ink: #555a5e;
    --paper: #ffffff;
    --backdrop: #e6e7e6;
  }
  * { margin: 0; padding: 0; box-sizing: border-box; }
  html, body {
    width: 1200px; height: 1200px; overflow: hidden;
    background: var(--backdrop);
    font-family: "Montserrat", sans-serif;
  }
  .card {
    position: absolute; left: 179px; width: 861px; height: 496px;
    background: var(--paper);
  }
  .card--front { top: 84px; }
  .card--back { top: 621px; }

  .brand { position: absolute; display: flex; align-items: center; }
  .brand__dot { border-radius: 50%; background: var(--navy); flex: none; }
  .brand__name {
    color: var(--navy); font-weight: 700; text-transform: uppercase;
    line-height: 1.02; letter-spacing: 0.04em;
  }
  .card--front .brand { left: 128px; top: 178px; gap: 28px; }
  .card--front .brand__dot { width: 142px; height: 142px; }
  .card--front .brand__name { font-size: 56px; }
  .card--back .brand { left: 40px; top: 65px; gap: 16px; }
  .card--back .brand__dot { width: 82px; height: 82px; }
  .card--back .brand__name { font-size: 33px; }

  .person { position: absolute; right: 46px; top: 70px; text-align: right; }
  .person__name { color: var(--navy); font-weight: 600; font-size: 25px; line-height: 1.2; }
  .person__title { color: var(--green); font-weight: 400; font-size: 22px; margin-top: 8px; }
  .tab {
    position: absolute; right: 0; top: 76px; width: 12px; height: 58px;
    background: var(--navy); border-radius: 5px 0 0 5px;
  }

  .offices { position: absolute; left: 40px; top: 244px; }
  .office + .office { margin-top: 8px; }
  .office__label { color: var(--navy); font-weight: 600; font-size: 22px; line-height: 30px; }
  .office__address { color: var(--ink); font-size: 21.5px; line-height: 30.5px; font-style: normal; }

  .contacts { position: absolute; right: 44px; top: 326px; list-style: none; }
  .contacts li {
    display: flex; justify-content: flex-end; align-items: center; gap: 7px;
    color: var(--ink); font-size: 22.5px; line-height: 37px; letter-spacing: 0.02em;
  }
  .contacts svg { width: 21px; height: 21px; fill: var(--green); flex: none; }
</style>
</head>
<body>
  <section class="card card--front">
    <div class="brand">
      <span class="brand__dot"></span>
      <span class="brand__name">Velmora<br>Arcs</span>
    </div>
  </section>

  <section class="card card--back">
    <div class="brand">
      <span class="brand__dot"></span>
      <span class="brand__name">Velmora<br>Arcs</span>
    </div>

    <div class="person">
      <p class="person__name">Dorian L. Whitcombe, ASLA</p>
      <p class="person__title">CEO &amp; Founder</p>
    </div>
    <span class="tab"></span>

    <div class="offices">
      <div class="office">
        <p class="office__label">West Region</p>
        <address class="office__address">4175 Quill Harbor Ln,<br>Suite #215 Englewood,<br>Colorado 80467</address>
      </div>
      <div class="office">
        <p class="office__label">East Region</p>
        <address class="office__address">3817 Tamsin Rd E,<br>Bradenton, Florida 34583</address>
      </div>
    </div>

    <ul class="contacts">
      <li>(303) 555-0174
        <svg viewBox="0 0 24 24" aria-hidden="true"><path d="M6.6 10.8a15 15 0 0 0 6.6 6.6l2.2-2.2c.3-.3.7-.4 1-.2 1.1.4 2.3.6 3.6.6.6 0 1 .4 1 1V20c0 .6-.4 1-1 1A17 17 0 0 1 3 4c0-.6.4-1 1-1h3.5c.6 0 1 .4 1 1 0 1.3.2 2.5.6 3.6.1.3 0 .7-.2 1z"/></svg>
      </li>
      <li>1-800-555-0139
        <svg viewBox="0 0 24 24" aria-hidden="true"><path d="M2 9c0-2 4.5-4 10-4s10 2 10 4v2h-5V9H7v2H2zM6 12h12l3 8H3zm6 2a2.5 2.5 0 1 0 0 5 2.5 2.5 0 0 0 0-5z"/></svg>
      </li>
      <li>dorian@velmoraarcs.com
        <svg viewBox="0 0 24 24" aria-hidden="true"><path d="M2 5h20v14H2zm2 2v.5l8 5 8-5V7zm0 3v7h16v-7l-8 5z"/></svg>
      </li>
      <li>www.velmoraarcs.com
        <svg viewBox="0 0 24 24" aria-hidden="true"><path d="M12 2a10 10 0 1 0 0 20 10 10 0 0 0 0-20zm-1 2.1V8H7.8c.7-2 1.9-3.5 3.2-3.9zm2 0c1.3.4 2.5 1.9 3.2 3.9H13zM6.8 5.6A8 8 0 0 0 5.2 8H4.9a8 8 0 0 1 1.9-2.4zM4.2 10h3.2a16 16 0 0 0 0 4H4.2a8 8 0 0 1 0-4zm5.2 0H11v4H9.4a14 14 0 0 1 0-4zM13 10h1.6a14 14 0 0 1 0 4H13zm3.6 0h3.2a8 8 0 0 1 0 4h-3.2a16 16 0 0 0 0-4zM4.9 16h2.9c.4 1 .9 1.8 1.5 2.6A8 8 0 0 1 4.9 16zm2.9-8zM9.4 16H11v3.9c-.7-.5-1.3-2.2-1.6-3.9zm3.6 0h1.6c-.3 1.7-.9 3.4-1.6 3.9zm3.2 0h2.9a8 8 0 0 1-4.4 2.6c.6-.8 1.1-1.6 1.5-2.6zm1.8-10.4A8 8 0 0 1 19.1 8h-.3a8 8 0 0 0-1.6-2.4z"/></svg>
      </li>
    </ul>
  </section>
</body>
</html>
```